Need Website for PR Firm

I need a website for my new business, Lantern Hill Agency, a PR, Communications and Marketing Firm. I want something classy and clean. Tailored and professional with a bit of a whimsical touch. Colors are mainly white and green. I don't like random stock photos but I would consider an image of a park with the city in the background. The name of my company is a play on Willowmere Green in Brooklyn where I am based.

The navigation and pages I will need is a good clean landing page.
About us
Who we are
Contact

Again, I like clean white and the copy in a similar color and font as my logo.
No stock photography or clip art.
I uploaded an image of the park that I like and wld be open to using in some way
Updates

I have uploaded an image of the park that you could implemented. 

Seeing some good designs here.

With the image I uploaded, I unfortunately think the green sky is too green.
Wondering if we can make modifications to the color of the sky.
I like the last image submitted too.

Target Market(s)

Professionals and the media who are seeing how I represent myself and my agency as they hire me for the public relations council.

Industry/Entity Type

Business

Font styles to use
Serif
Other font styles liked:
• Trajan

Colors
acd036
ffffff
dbdbdb
eeeeee

Requirements
Must have
• High quality and consistent colors and font.
Should not have
• Stock photography
Clip art
colors that aren't white, the green in my font, black or gray if necessary.

```html
<!DOCTYPE html>
<html lang="en">
<head>
<meta charset="utf-8">
<title>Lantern Hill Agency — Website Pages</title>
<link rel="stylesheet" href="https://fonts.googleapis.com/css2?family=Tinos:wght@400;700&display=swap">
<style>
  :root {
    --brand-green: #acd036;
    --accent-green: #8fb320;
    --page-bg: #e1e4ec;
    --band-bg: #cfd5e2;
    --panel-bg: #eeeeee;
    --content-grey: #dbdbdb;
    --rule: #d2d2d2;
    --nav-text: #777777;
    --wordmark-text: #5e5e5e;
    --heading-text: #707070;
    --body-text: #9a9a9a;
    --dark-ground: #363636;
    --white: #ffffff;
  }
  * { margin: 0; padding: 0; box-sizing: border-box; }
  html, body { width: 1200px; height: 591px; overflow: hidden; }
  body {
    position: relative;
    background: var(--page-bg);
    font-family: "Tinos", "Times New Roman", serif;
  }
  .band {
    position: absolute; left: 0; width: 1200px;
    background: linear-gradient(to bottom, var(--band-bg), rgba(207,213,226,0));
  }
  .band--top { top: 0; height: 30px; }
  .band--mid { top: 286px; height: 34px; }
  .floor-shadow {
    position: absolute; height: 8px; border-radius: 50%;
    background: radial-gradient(ellipse at center, rgba(120,128,145,.55), rgba(120,128,145,0) 70%);
  }
  .page {
    position: absolute; width: 363px;
    background: var(--panel-bg);
    box-shadow: 0 0 1px rgba(0,0,0,.12);
  }
  .sidebar { position: absolute; left: 0; top: 0; width: 81px; height: 100%; }
  .brand {
    position: absolute; left: 8px; top: 20px; width: 70px;
    display: flex; align-items: center; gap: 4px;
  }
  .brand__mark {
    flex: none; width: 6px; height: 6px; background: var(--accent-green);
  }
  .brand__name {
    color: var(--wordmark-text); font-size: 7px; line-height: 8px;
    white-space: nowrap;
  }
  .nav { position: absolute; left: 6px; top: 49px; width: 75px; list-style: none; }
  .nav__item {
    position: relative; height: 15.5px; line-height: 14px;
    text-align: center; font-size: 4.6px; color: var(--nav-text);
    text-transform: uppercase; letter-spacing: .1px;
    border-bottom: 1.5px solid var(--rule);
  }
  .nav__item:first-child { border-top: 1px solid var(--rule); }
  .nav__item--active { color: var(--accent-green); }
  .nav__tab {
    position: absolute; right: -9px; top: -1px; width: 9px; height: 15px;
    background: var(--white); box-shadow: 1px 0 1px rgba(0,0,0,.12);
  }
  .nav__tab::after {
    content: ""; position: absolute; left: 3px; top: 5.5px;
    border-left: 3px solid #888; border-top: 2px solid transparent; border-bottom: 2px solid transparent;
  }
  .social {
    position: absolute; left: 5px; top: 131px; width: 71px; height: 19px;
    background: var(--content-grey);
    display: flex; justify-content: space-around; align-items: center; padding: 0 6px;
  }
  .social__slot { width: 10px; height: 10px; background: var(--white); }
  .legal {
    position: absolute; left: 0; top: 170px; width: 81px;
    text-align: center; font-size: 3.2px; line-height: 10px; color: #aaaaaa;
  }
  .content {
    position: absolute; left: 81px; background: var(--content-grey);
    padding: 12px 14px; overflow: hidden;
  }
  .content__title { font-size: 5.6px; color: var(--heading-text); margin-bottom: 8px; font-weight: 400; }
  .content__heading { font-size: 5.2px; color: var(--heading-text); margin: 7px 0 7px; font-weight: 400; }
  .content__text { font-size: 5.2px; line-height: 9.6px; color: var(--body-text); }
  .feature {
    position: absolute; left: 81px; top: 2px; width: 277px; height: 209px;
    background: var(--brand-green); overflow: hidden;
  }
  .feature__kicker { position: absolute; left: 7px; top: 4px; font-size: 8px; font-weight: 700; color: #dfeaa0; }
  .feature__label { position: absolute; left: 7px; top: 14px; font-size: 3.6px; font-weight: 700; color: var(--white); letter-spacing: .3px; }
  .feature__title { position: absolute; left: 167px; top: 31px; font-size: 7px; font-weight: 700; color: var(--white); }
  .feature__copy { position: absolute; left: 175px; width: 92px; font-size: 4.4px; line-height: 7.6px; color: var(--white); }
  .feature__scene {
    position: absolute; left: 0; top: 92px; width: 277px; height: 117px;
    background: linear-gradient(to bottom, #acd036 0%, #9bb84a 30%, #b9bf98 48%, #e6e6df 56%, var(--dark-ground) 60%, var(--dark-ground) 100%);
  }
</style>
</head>
<body>
  <div class="band band--top"></div>
  <div class="band band--mid"></div>

  <div class="floor-shadow" style="left:175px; top:271px; width:255px;"></div>
  <div class="floor-shadow" style="left:772px; top:274px; width:255px;"></div>
  <div class="floor-shadow" style="left:174px; top:565px; width:255px;"></div>
  <div class="floor-shadow" style="left:772px; top:511px; width:255px;"></div>

  <!-- Home page -->
  <section class="page" style="left:120px; top:26px; height:241px;">
    <aside class="sidebar">
      <div class="brand"><span class="brand__mark"></span><span class="brand__name">Lantern Hill Agency</span></div>
      <ul class="nav">
        <li class="nav__item nav__item--active">Home<span class="nav__tab"></span></li>
        <li class="nav__item">About</li>
        <li class="nav__item">Who we are</li>
        <li class="nav__item">Contact</li>
      </ul>
      <div class="social"><span class="social__slot"></span><span class="social__slot"></span><span class="social__slot"></span></div>
      <p class="legal">© Copyright 2011<br>Lantern Hill Agency all rights reserved</p>
    </aside>
    <div class="feature">
      <p class="feature__kicker">please wake me up !</p>
      <p class="feature__label">CROSS SECTION</p>
      <h2 class="feature__title">Text text</h2>
      <p class="feature__copy" style="top:47px;">Text text text text text text text text text text text text text text text text.</p>
      <p class="feature__copy" style="top:71px;">Text text text text text text text text text text text text text text text text text text text text text text text.</p>
      <div class="feature__scene" role="img" aria-label="Cross-section illustration of Willowmere Green with trees, an arch, people and traffic lanes below"></div>
    </div>
  </section>

  <!-- About page -->
  <section class="page" style="left:718px; top:24px; height:246px;">
    <aside class="sidebar">
      <div class="brand"><span class="brand__mark"></span><span class="brand__name">Lantern Hill Agency</span></div>
      <ul class="nav">
        <li class="nav__item">Home</li>
        <li class="nav__item nav__item--active">About<span class="nav__tab"></span></li>
        <li class="nav__item">Who we are</li>
        <li class="nav__item">Contact</li>
      </ul>
      <div class="social"><span class="social__slot"></span><span class="social__slot"></span><span class="social__slot"></span></div>
      <p class="legal">© Copyright 2011<br>Lantern Hill Agency all rights reserved</p>
    </aside>
    <article class="content" style="top:2px; width:278px; height:224px;">
      <h2 class="content__title">Text text text&nbsp; text text&nbsp; text text&nbsp; text text&nbsp; text text</h2>
      <p class="content__text">Text text text text text text text text text text text text text text text text text text text text text text text text text text text text text text text text text text text text text text text text text text text text text text text text text text text text text text text text text text text text text text text text text text text text text text text text text text text text text text text text.</p>
      <h3 class="content__heading">Text text text</h3>
      <p class="content__text">Text text text text text text text text text text text text text text text text text text text text text text text text text text text text text text text text text text text text text text text text text text text text text text text text text text text text text text text text text text text.</p>
      <h3 class="content__heading">Text</h3>
      <p class="content__text">Text text text text text text text text text text text text text text text text text text text text text text text text text text text text text text text text text text text text text text.</p>
      <h3 class="content__heading">Text</h3>
      <p class="content__text">text text text text text text text text text text text text text text text text text text text text text text text text text text text text text text text text text text text text text text text text text text text text text text text text text text text text text text text text text text.</p>
    </article>
  </section>

  <!-- Who we are page -->
  <section class="page" style="left:119px; top:314px; height:248px;">
    <aside class="sidebar">
      <div class="brand"><span class="brand__mark"></span><span class="brand__name">Lantern Hill Agency</span></div>
      <ul class="nav">
        <li class="nav__item">Home</li>
        <li class="nav__item">About</li>
        <li class="nav__item">Who we are</li>
        <li class="nav__item">Contact</li>
      </ul>
      <div class="social"><span class="social__slot"></span><span class="social__slot"></span><span class="social__slot"></span></div>
      <p class="legal">© Copyright 2011<br>Lantern Hill Agency all rights reserved</p>
    </aside>
    <article class="content" style="top:4px; width:278px; height:222px;">
      <h2 class="content__title">Text text text&nbsp; text text&nbsp; text text&nbsp; text text&nbsp; text text</h2>
      <p class="content__text">Text text text text text text text text text text text text text text text text text text text text text text text text text text text text text text text text text text text text text text text text text text text text text text text text text text text text text text text text text text text text text text text text text text text text text text text text text text text text text text text text.</p>
      <h3 class="content__heading">Text text text</h3>
      <p class="content__text">Text text text text text text text text text text text text text text text text text text text text text text text text text text text text text text text text text text text text text text text text text text text text text text text text text text text text text text text text text text text.</p>
      <h3 class="content__heading">Text</h3>
      <p class="content__text">Text text text text text text text text text text text text text text text text text text text text text text text text text text text text text text text text text text text text text text.</p>
      <h3 class="content__heading">Text</h3>
      <p class="content__text">text text text text text text text text text text text text text text text text text text text text text text text text text text text text text text text text text text text text text text text text text text text text text text text text text text text text text text text text text text.</p>
    </article>
  </section>

  <!-- Contact page -->
  <section class="page" style="left:718px; top:316px; height:191px;">
    <aside class="sidebar">
      <div class="brand"><span class="brand__mark"></span><span class="brand__name">Lantern Hill Agency</span></div>
      <ul class="nav">
        <li class="nav__item">Home</li>
        <li class="nav__item">About</li>
        <li class="nav__item">Who we are</li>
        <li class="nav__item nav__item--active">Contact<span class="nav__tab"></span></li>
      </ul>
      <div class="social"><span class="social__slot"></span><span class="social__slot"></span><span class="social__slot"></span></div>
      <p class="legal">© Copyright 2011<br>Lantern Hill Agency all rights reserved</p>
    </aside>
    <article class="content" style="top:2px; width:278px; height:134px;">
      <h2 class="content__title">Text text text&nbsp; text text&nbsp; text text&nbsp; text text&nbsp; text text</h2>
      <p class="content__text">Text text text text text text text text text text text text text text text text text text text text text text text text text text text text text text text text text text text text text text text text text text text text text text text text text text text text text text text text text text text text text text text text text text text text text text text text text text.</p>
      <h3 class="content__heading">Text text text&nbsp; text text&nbsp; text text&nbsp; text text</h3>
      <p class="content__text">Text text text text text text text text text text text text text text text text text text text text text text text text text text text text text text text text text text text text text text text text text text text text text text text text text text text text text text text text text text text text text text text text text text text text text text text text text text.</p>
    </article>
  </section>
</body>
</html>
```